New Business Card Design Project

We want a modern business card that catches the attention of other remodeling companies as well as homeowners. We would like it to be informative but still simple.

Target Market(s)

Residential and other Business's

Contact Information for Business Card

TrellBrix
Phone number is 5153927048
Address is
4817 SW 3rd Lane
Des Moines, Iowa 50313
email is trellbrixco@quamlet.com

Requirements
Must have
• Our tagline
• Honest | Professional | Affordable

```html
<!DOCTYPE html>
<html lang="en">
<head>
<meta charset="utf-8">
<title>TrellBrix Business Card</title>
<link rel="stylesheet" href="https://fonts.googleapis.com/css2?family=Montserrat:wght@400;500;700&display=swap">
<style>
  :root {
    --brand-blue: #0a63c6;
    --card-blue: #0066c8;
    --accent-orange: #d0541a;
    --paper: #f7f7f7;
    --page-bg: #e9e9e9;
    --white: #ffffff;
  }
  * { margin: 0; padding: 0; box-sizing: border-box; }
  html, body { width: 1200px; height: 900px; overflow: hidden; }
  body {
    background: var(--page-bg);
    font-family: "Montserrat", sans-serif;
    position: relative;
  }
  .card {
    position: absolute;
    left: 285px;
    width: 630px;
    height: 360px;
    overflow: hidden;
    box-shadow: 0 6px 18px rgba(0,0,0,0.15);
  }
  .card-front { top: 50px; background: var(--paper); }
  .card-back { top: 480px; background: var(--card-blue); }

  .front-name {
    position: absolute;
    left: 38px;
    top: 70px;
    font-weight: 700;
    font-size: 32px;
    letter-spacing: 1px;
    color: var(--brand-blue);
    line-height: 1;
  }

  .person {
    position: absolute;
    left: 60px;
    top: 190px;
  }
  .person-name {
    font-weight: 500;
    font-size: 31px;
    letter-spacing: 2.5px;
    color: var(--brand-blue);
    text-transform: uppercase;
    line-height: 1;
  }
  .person-title {
    font-weight: 500;
    font-size: 14px;
    letter-spacing: 5px;
    color: var(--accent-orange);
    text-transform: uppercase;
    margin-top: 6px;
    padding-left: 70px;
  }

  .contact-list {
    position: absolute;
    left: 420px;
    top: 178px;
    border-left: 2px solid var(--accent-orange);
    padding-left: 14px;
    list-style: none;
  }
  .contact-item {
    display: flex;
    align-items: center;
    gap: 12px;
    height: 38px;
    font-size: 11px;
    color: var(--brand-blue);
    line-height: 1.35;
  }
  .contact-item svg { width: 16px; height: 16px; flex: none; fill: var(--accent-orange); }

  .front-values {
    position: absolute;
    left: 38px;
    bottom: 30px;
    font-size: 11px;
    font-weight: 500;
    letter-spacing: 2px;
    color: var(--accent-orange);
    text-transform: uppercase;
  }

  .back-name {
    position: absolute;
    left: 0;
    right: 0;
    top: 120px;
    text-align: center;
    color: var(--white);
    font-weight: 700;
    font-size: 66px;
    letter-spacing: 2px;
    line-height: 1;
  }
  .back-values {
    position: absolute;
    left: 0;
    right: 0;
    bottom: 40px;
    text-align: center;
    color: var(--white);
    font-weight: 400;
    font-size: 14px;
    letter-spacing: 3px;
    text-transform: uppercase;
  }
</style>
</head>
<body>

<section class="card card-front">
  <div class="front-name">TRELLBRIX</div>

  <div class="person">
    <div class="person-name">Darian Kessler</div>
    <div class="person-title">General Manager</div>
  </div>

  <ul class="contact-list">
    <li class="contact-item">
      <svg viewBox="0 0 24 24" aria-hidden="true"><path d="M12 2a7 7 0 0 0-7 7c0 5.2 7 13 7 13s7-7.8 7-13a7 7 0 0 0-7-7zm0 9.5A2.5 2.5 0 1 1 12 6.5a2.5 2.5 0 0 1 0 5z"/></svg>
      <span>4817 SW 3rd Lane<br>Des Moines, Iowa 50313</span>
    </li>
    <li class="contact-item">
      <svg viewBox="0 0 24 24" aria-hidden="true"><path d="M6.6 10.8a15.1 15.1 0 0 0 6.6 6.6l2.2-2.2a1 1 0 0 1 1-.25 11.4 11.4 0 0 0 3.6.57 1 1 0 0 1 1 1V20a1 1 0 0 1-1 1A17 17 0 0 1 3 4a1 1 0 0 1 1-1h3.5a1 1 0 0 1 1 1c0 1.25.2 2.45.57 3.57a1 1 0 0 1-.25 1z"/></svg>
      <span>515 - 392 - 7048</span>
    </li>
    <li class="contact-item">
      <svg viewBox="0 0 24 24" aria-hidden="true"><path d="M2 5h20v14H2z"/><path d="M3 6l9 7 9-7" fill="none" stroke="#f7f7f7" stroke-width="1.5"/></svg>
      <span>trellbrixco@quamlet.com</span>
    </li>
  </ul>

  <p class="front-values">Honest · Professional · Affordable</p>
</section>

<section class="card card-back">
  <div class="back-name">TRELLBRIX</div>
  <p class="back-values">Honest · Professional · Affordable</p>
</section>

</body>
</html>
```